Tile installation contractor -business card design

We are a tile contractor doing installation of tile on floors, walls, we tile showers, backsplashes, kitchens, entry ways. we install all types of tile ceramic, porcelain, travertine, marble, slate ect. we also do demolition and tear outs of old existing tile (removal) we do commercial, or residential jobs. tile and grout repairs. sealing of grout/tile. small or large jobs. we are fast, clean, do quality work, honest and hard working. anything tile we can do. design or patterns. we do shower pans and all prep work needed to install tile. fair competitive pricing
Industry/Entity Type
Business
Contact Information for Business Card
Granvale Tile- company name
Dean Ruskin/ owner 801-555-2943
granvale_tile@quormail.net
Free Estimates
Clinton Utah, 84099
20+ years experience
Licensed and Insured

```html
<!DOCTYPE html>
<html lang="en">
<head>
<meta charset="utf-8">
<title>Granvale Tile – Business Card</title>
<link href="https://fonts.googleapis.com/css2?family=Nunito:wght@800&family=Open+Sans:wght@300;400&display=swap" rel="stylesheet">
<style>
  :root {
    --page-bg: #e9e4dc;
    --card-white: #ffffff;
    --ink-dark: #2b2723;
    --ink-body: #3a3a3a;
    --tile-light: #f1e2c4;
    --tile-mid: #d9b97f;
    --tile-deep: #b88a45;
    --card-shadow: rgba(60, 40, 20, 0.28);
  }
  html, body {
    margin: 0;
    padding: 0;
    width: 1200px;
    height: 1023px;
    overflow: hidden;
    background: var(--page-bg);
  }
  .canvas {
    width: 1200px;
    height: 1023px;
    display: flex;
    flex-direction: column;
    align-items: center;
    justify-content: center;
    gap: 70px;
  }
  .card {
    position: relative;
    width: 560px;
    height: 320px;
    border-radius: 4px;
    overflow: hidden;
    box-shadow: 0 10px 28px var(--card-shadow);
  }
  .card-front .photo-fill {
    position: absolute;
    inset: 0;
    background:
      radial-gradient(ellipse at 70% 75%, rgba(184,138,69,0.55), transparent 60%),
      linear-gradient(120deg, var(--tile-light) 0%, var(--tile-mid) 55%, var(--tile-deep) 100%);
  }
  .card-front .company-name {
    position: absolute;
    left: 0;
    right: 0;
    top: 50%;
    transform: translateY(-50%);
    margin: 0;
    text-align: center;
    font-family: "Nunito", sans-serif;
    font-weight: 800;
    font-size: 50px;
    letter-spacing: 1px;
    color: var(--ink-dark);
  }
  .card-back {
    background: var(--card-white);
  }
  .card-back .contact {
    position: absolute;
    left: 250px;
    top: 110px;
    font-family: "Open Sans", sans-serif;
    font-weight: 300;
    color: var(--ink-body);
    font-size: 20px;
    line-height: 34px;
  }
  .card-back .contact p { margin: 0; }
  .card-back .owner-name { font-weight: 400; }
</style>
</head>
<body>
  <main class="canvas">
    <section class="card card-front">
      <div class="photo-fill" role="img" aria-label="Photo of a finished tiled shower with travertine walls, a bench and a pebble stone floor"></div>
      <h1 class="company-name">Granvale Tile</h1>
    </section>
    <section class="card card-back">
      <div class="contact">
        <p class="owner-name">Dean Ruskin</p>
        <p class="phone">801-555-2943</p>
        <p class="email">granvale_tile@quormail.net</p>
      </div>
    </section>
  </main>
</body>
</html>
```